Letter and Envelope Design For Larchmont Realty

Please design a letter and an envelope incorporating our logo (See Attached). We are also launched a business card contest. Since we want them to match, please feel free to submit a design for both the business card and also the letter design and envelope.

Requirements
Must have
• The envelope, the letter and the business cards must match somehow connecting the designs. We want them to have something that holds them together besides the logo.

```html
<!DOCTYPE html>
<html lang="en">
<head>
<meta charset="utf-8">
<title>Larchmont Realty Stationery</title>
<link href="https://fonts.googleapis.com/css2?family=Montserrat:wght@500;600&family=Mulish:wght@400;600;700&display=swap" rel="stylesheet">
<style>
:root{
  --navy:#27306f;
  --slate:#58585a;
  --paper:#ffffff;
  --backdrop:#d2d2d2;
  --ink:#4a4a4a;
  --faint:#f0f0f0;
}
*{margin:0;padding:0;box-sizing:border-box}
html,body{width:1200px;height:1200px;overflow:hidden;background:var(--backdrop)}
body{position:relative;font-family:"Mulish",sans-serif;color:var(--ink)}
.sheet{position:absolute;background:var(--paper);box-shadow:0 2px 4px rgba(0,0,0,.18);overflow:hidden}
.bar{position:absolute;top:0;height:9px}
.bar-navy{background:var(--navy)}
.bar-slate{background:var(--slate)}
.brand{position:absolute;text-align:center;color:var(--navy);font-family:"Montserrat",sans-serif;font-weight:600;line-height:1}
.brand-ring{display:block;margin:0 auto;border:3px solid var(--navy);border-radius:50%}
.brand-name{display:block;letter-spacing:.14em}
.brand-sub{display:block;letter-spacing:.4em}
.watermark{position:absolute;border:7px solid var(--faint);border-radius:50%}
.contact{list-style:none;color:#fff;font-size:10px;line-height:1.3}
.contact li{display:flex;align-items:flex-start;gap:4px}
.contact svg{flex:none;margin-top:2px;fill:#fff}

/* letter */
.letter{left:50px;top:166px;width:538px;height:759px}
.letter .bar-navy{left:0;width:348px}
.letter .bar-slate{left:354px;width:184px}
.letter-body{position:absolute;left:59px;top:258px;width:410px;font-size:10.4px;line-height:13px}
.letter-body .salutation{color:var(--navy);font-weight:600;margin-bottom:13px}
.letter-body p{margin-bottom:13px}
.letter-footer{position:absolute;left:0;top:682px;width:538px;height:62px;background:var(--slate);color:#fff;font-size:10.4px;line-height:13.5px;text-align:center;padding-top:14px}
.letter-footer span{display:inline-flex;align-items:center;gap:3px;margin:0 3px}
.letter-footer svg{fill:#fff}

/* cards */
.card{left:610px;width:265px;height:152px}
.card-front{top:169px}
.card-front .bar{height:5px}
.card-front .bar-navy{left:0;width:172px}
.card-front .bar-slate{left:176px;width:89px}
.card-back{top:333px}
.card-panel{position:absolute;left:144px;top:0;width:121px;height:152px;background:var(--slate);color:#fff;padding:30px 0 0 9px}
.card-name{font-family:"Montserrat",sans-serif;font-weight:600;font-size:11.5px}
.card-role{font-size:7.5px;margin:1px 0 20px}
.card-panel .contact{font-size:6.5px;line-height:1.35}
.card-panel .contact svg{margin-top:1px}

/* envelope */
.envelope{left:619px;top:666px;width:535px;height:261px}
.flap{position:absolute;left:619px;top:580px}
.env-strip{position:absolute;top:0;height:8px}
.env-contact{position:absolute;left:354px;top:155px;width:181px;height:83px;background:var(--slate);padding:11px 0 0 10px}
.env-contact .contact{font-size:9.5px;line-height:1.28}
</style>
</head>
<body>

<section class="sheet letter" aria-label="Letterhead">
  <div class="bar bar-navy"></div>
  <div class="bar bar-slate"></div>
  <div class="brand" style="left:169px;top:56px;width:200px">
    <span class="brand-ring" style="width:68px;height:68px"></span>
    <span class="brand-name" style="font-size:18px;margin-top:6px">LARCHMONT</span>
    <span class="brand-sub" style="font-size:12px;margin-top:4px">REALTY</span>
  </div>
  <div class="watermark" style="left:141px;top:218px;width:256px;height:256px"></div>
  <div class="letter-body">
    <p class="salutation">Dear Mr. Daniel Reyes,</p>
    <p>Lorem ipsum dolor sit amet, consectetuer adipiscing elit, sed diam nonummy nibh euismod tincidunt ut laoreet dolore magna aliquam erat volutpat. Ut wisi enim ad minim veniam, quis nostrud exerci tation ullamcorper suscipit lobortis nisl ut aliquip ex ea commodo consequat. Duis autem vel eum iriure dolor in hendrerit in vulputate velit esse molestie consequat, vel illum dolore eu feugiat nulla facilisis at vero eros et accumsan et iusto odio dignissim qui blandit praesent luptatum zzril</p>
    <p>Lorem ipsum dolor sit amet, cons ectetuer adipiscing elit, sed diam nonummy nibh euismod tincidunt ut laoreet dolore magna aliquam erat volutpat. Ut wisi enim ad minim veniam, quis nostrud exerci tation ullamcorper suscipit lobortis nisl ut aliquip ex ea commodo consequat.</p>
    <p>Lorem ipsum dolor sit amet, consectetuer adipiscing elit, sed diam nonummy nibh euismod tincidunt ut laoreet dolore magna aliquam erat volutpat. Ut wisi enim ad minim veniam, quis nostrud exerci tation ullamcorper suscipit lobortis nisl ut aliquip ex ea commodo consequat. Duis autem vel eum iriure dolor in hendrerit in vulputate velit esse molestie consequat, vel illum dolore eu feugiat nulla facilisis at vero eros et accum</p>
    <p>Lorem ipsum dolor sit amet, consectetuer adipiscing elit, sed diam nonummy nibh euismod tincidunt ut laoreet dolore magna aliquam erat volutpat.</p>
    <p>Best Regards,<br>Your Name</p>
  </div>
  <footer class="letter-footer">
    <span><svg width="9" height="9" viewBox="0 0 10 10"><rect x="0" y="0" width="10" height="10" rx="2"/><path d="M3 2l1.3 1.8-.8.8c.5 1 1.1 1.6 2 2l.8-.8L8 7.2 7 8.2C4.4 7.6 2.5 5.7 1.9 3z" fill="#58585a"/></svg>(000)-5550-182</span>
    <span><svg width="9" height="9" viewBox="0 0 10 10"><rect x="0" y="0" width="10" height="10" rx="2"/><path d="M2 3h6v4H2zM2 3l3 2.3L8 3" fill="none" stroke="#58585a" stroke-width="1"/></svg>info@larchmontrealty.example</span><br>
    <span><svg width="7" height="10" viewBox="0 0 7 10"><path d="M3.5 0A3.5 3.5 0 0 0 0 3.5C0 6 3.5 10 3.5 10S7 6 7 3.5A3.5 3.5 0 0 0 3.5 0zm0 5a1.4 1.4 0 1 1 0-2.8 1.4 1.4 0 0 1 0 2.8z"/></svg>Street Address Here, Cedarvale, 00000 USA</span><br>
    <span><svg width="9" height="9" viewBox="0 0 10 10"><circle cx="5" cy="5" r="5"/><path d="M0 5h10M5 0c-2 2.5-2 7.5 0 10M5 0c2 2.5 2 7.5 0 10" fill="none" stroke="#58585a" stroke-width=".8"/></svg>www.larchmontrealty.example</span>
  </footer>
</section>

<section class="sheet card card-front" aria-label="Business card front">
  <div class="bar bar-navy"></div>
  <div class="bar bar-slate"></div>
  <div class="brand" style="left:52px;top:34px;width:160px">
    <span class="brand-ring" style="width:54px;height:54px;border-width:2.5px"></span>
    <span class="brand-name" style="font-size:14.5px;margin-top:6px">LARCHMONT</span>
    <span class="brand-sub" style="font-size:10px;margin-top:4px">REALTY</span>
  </div>
</section>

<section class="sheet card card-back" aria-label="Business card back">
  <div class="brand" style="left:12px;top:42px;width:122px">
    <span class="brand-ring" style="width:36px;height:36px;border-width:2px"></span>
    <span class="brand-name" style="font-size:10px;margin-top:6px">LARCHMONT</span>
    <span class="brand-sub" style="font-size:7px;margin-top:3px">REALTY</span>
  </div>
  <div class="card-panel">
    <div class="card-name">DANIEL REYES</div>
    <div class="card-role">Chief executive officer</div>
    <ul class="contact">
      <li><svg width="6" height="6" viewBox="0 0 10 10"><rect width="10" height="10" rx="2"/></svg>(000)-5550-182</li>
      <li><svg width="6" height="6" viewBox="0 0 10 10"><rect width="10" height="10" rx="2"/></svg>info@larchmontrealty.example</li>
      <li><svg width="5" height="7" viewBox="0 0 7 10"><path d="M3.5 0A3.5 3.5 0 0 0 0 3.5C0 6 3.5 10 3.5 10S7 6 7 3.5A3.5 3.5 0 0 0 3.5 0z"/></svg>Street Address Here,<br>Cedarvale, 00000 USA</li>
      <li><svg width="6" height="6" viewBox="0 0 10 10"><circle cx="5" cy="5" r="5"/></svg>www.larchmontrealty.example</li>
    </ul>
  </div>
</section>

<section class="sheet envelope" aria-label="Envelope">
  <div class="env-strip" style="left:0;width:347px;background:var(--navy)"></div>
  <div class="env-strip" style="left:354px;width:181px;background:var(--slate)"></div>
  <div class="brand" style="left:15px;top:10px;width:140px">
    <span class="brand-ring" style="width:52px;height:52px;border-width:2.5px"></span>
    <span class="brand-name" style="font-size:14.5px;margin-top:8px">LARCHMONT</span>
    <span class="brand-sub" style="font-size:10px;margin-top:4px">REALTY</span>
  </div>
  <div class="watermark" style="left:173px;top:34px;width:188px;height:188px;border-width:5px"></div>
  <div class="env-contact">
    <ul class="contact">
      <li><svg width="8" height="8" viewBox="0 0 10 10"><rect width="10" height="10" rx="2"/></svg>(000)-5550-182</li>
      <li><svg width="8" height="8" viewBox="0 0 10 10"><rect width="10" height="10" rx="2"/></svg>info@larchmontrealty.example</li>
      <li><svg width="6" height="9" viewBox="0 0 7 10"><path d="M3.5 0A3.5 3.5 0 0 0 0 3.5C0 6 3.5 10 3.5 10S7 6 7 3.5A3.5 3.5 0 0 0 3.5 0z"/></svg>Street Address Here,<br>Cedarvale, 00000 USA</li>
      <li><svg width="8" height="8" viewBox="0 0 10 10"><circle cx="5" cy="5" r="5"/></svg>www.larchmontrealty.example</li>
    </ul>
  </div>
</section>

<svg class="flap" width="535" height="86" viewBox="0 0 535 86" aria-label="Envelope flap">
  <polygon points="19,0 515,0 535,78 0,78" fill="var(--navy)"/>
  <g transform="rotate(180 267 37)" fill="#fff" font-family="Montserrat, sans-serif" font-weight="600">
    <circle cx="209" cy="34" r="19" fill="none" stroke="#fff" stroke-width="2.5"/>
    <text x="291" y="37" font-size="11" letter-spacing="1.5" text-anchor="middle">LARCHMONT</text>
    <text x="291" y="48" font-size="7.5" letter-spacing="3" text-anchor="middle">REALTY</text>
  </g>
</svg>

</body>
</html>
```